Flyer
Zielgruppe
Brandl´s Werkhaus Holz+ Design
Schreinerei
- aus alt mach neu! wir möchten alte Küchen in neuem Glanz erscheinen lassen.
Fronten/ Griffe / Scharniere/ Beleuchtung Arbeitsplatten werden nach Wunsch erneuert
- neue Türen- nach Wunsch restauriert oder neu eingebaut
- Möbelbau auf Maß
Zielgruppe sind:
- Hausbesitzer/ Eigenheimbesitzer
-älteres Publikum
Aufgabenstellung
- der Fleyer soll übersichtlich sein- bitte nur Deutsche Sprache verwenden
- gern zweiseitig ( wir möchen jeden Monat etwas neues bewerben)
- die eine Seite hat ein festes Layout wo folgende Infos zu entnehmen sind:
BITTE! diesen text auf den Fleyer platzieren:
Brandl`s Werkhaus Holz & Design
Ihre Schreinerei aus Mannheim:
Wir fertigen oder reparieren Ihre Traummöbel aus Holz:
Schlafzimmer
Küchen / Esszimmer
Büromöbel
Wohnmöbel
TreppeTüren
Kaminverkleidungen
Sonderanfertigungen
Bitte halten sie sich an die Webseite- Farbthema usw.
+ Bitte nehmen Sie die vorher nachher Fotos - der Zusammenhang muss stimmen
- keine langen Texte mit einfügen- kurz klar und auf den Punkt bringen
Telefonnumer : 0621 5918207
WICHITG: Frühjahr - Rabattaktion soll mit drauf 15 % auf Ihre neue Küche gültig bis zum 01.05-2025

```html
<!DOCTYPE html>
<html lang="de">
<head>
<meta charset="utf-8">
<title>Brandl's Werkhaus – Flyer</title>
<link href="https://fonts.googleapis.com/css2?family=Inter:wght@400;500;700&display=swap" rel="stylesheet">
<style>
  :root {
    --bg: #ebebeb;
    --paper: #ffffff;
    --paper-grey: #efefef;
    --ink: #262626;
    --dark: #2b2b2b;
    --white: #ffffff;
  }
  * { margin: 0; padding: 0; box-sizing: border-box; }
  html, body { width: 1080px; height: 1200px; overflow: hidden; }
  body {
    background: var(--bg);
    font-family: "Inter", Arial, sans-serif;
    color: var(--ink);
    position: relative;
  }
  .flyer {
    position: absolute;
    top: 245px;
    width: 500px;
    height: 710px;
    background: var(--paper);
    overflow: hidden;
    box-shadow: 0 6px 22px rgba(0,0,0,.10);
  }
  .flyer--front { left: 25px; }
  .flyer--back { left: 555px; background: var(--paper-grey); }

  /* Front */
  .hero-photo {
    position: absolute; left: 0; top: 0; width: 500px; height: 344px;
    background: linear-gradient(180deg, #e9eef0 0%, #d7dcdf 45%, #8d8f92 70%, #3a3a3a 100%);
  }
  .brand-box {
    position: absolute; left: 0; top: 0; width: 197px; height: 74px;
    background: var(--dark);
    display: flex; align-items: center; justify-content: center;
  }
  .brand-name {
    color: var(--white); font-weight: 700; font-size: 14px;
    letter-spacing: 1.5px; text-transform: uppercase;
  }
  .contact-area {
    position: absolute; left: 0; top: 570px; width: 500px; height: 140px;
    background: var(--paper-grey);
  }
  .headline {
    position: absolute; font-size: 40px; line-height: 38px;
    font-weight: 400; letter-spacing: -1px; white-space: nowrap;
  }
  .headline b { font-weight: 700; }
  .subline {
    position: absolute; font-size: 15.5px; line-height: 16px; font-weight: 400; white-space: nowrap;
  }
  .services { position: absolute; left: 282px; top: 418px; width: 182px; list-style: none; }
  .service {
    height: 34px; margin-bottom: 11px; background: var(--dark); color: var(--white);
    display: flex; align-items: center; font-size: 13px; font-weight: 400;
  }
  .service svg { width: 22px; height: 22px; margin: 0 16px 0 12px; flex: none; }
  .contact-title { position: absolute; font-size: 14.5px; font-weight: 700; }
  .contact-address { position: absolute; font-size: 10.5px; line-height: 12.5px; }
  .phone-button {
    position: absolute; width: 182px; height: 34px;
    display: flex; align-items: center; font-size: 13px; font-weight: 500;
  }
  .phone-button svg { width: 20px; height: 20px; margin: 0 30px 0 12px; }
  .phone-button--dark { background: var(--dark); color: var(--white); }
  .phone-button--light { background: var(--white); color: var(--ink); }
  .website {
    position: absolute; left: 0; width: 500px; top: 674px; text-align: center;
    font-size: 9.5px; letter-spacing: 9px; text-transform: uppercase;
  }

  /* Back */
  .project-grid {
    position: absolute; left: 0; top: 6px; width: 500px; height: 350px;
    display: grid; grid-template-columns: 61px 169px 171px 75px;
    grid-template-rows: 171px 171px; gap: 8px;
    background: var(--white);
  }
  .project-photo--wood { background: linear-gradient(160deg, #c98a4e, #8c5a2e 60%, #e3d7c6); }
  .project-photo--steel { background: linear-gradient(160deg, #d9d9d9, #8f9396 55%, #5b5e61); }
  .project-photo--grey { background: linear-gradient(160deg, #b9bec3, #6e7378 60%, #3d3f42); }
  .project-photo--green { background: linear-gradient(160deg, #8fe3cf, #5c6a66 55%, #cfcfd4); }
  .project-photo--white { background: linear-gradient(160deg, #e7e7e7, #bdbfc2 60%, #7a5a3b); }
  .back-brand {
    position: absolute; left: 40px; top: 380px;
    font-size: 14px; font-weight: 700; letter-spacing: 1.5px; text-transform: uppercase;
  }
  .workshop-intro {
    position: absolute; left: 40px; top: 403px;
    font-size: 10.5px; font-weight: 500; line-height: 13px;
  }
  .workshop-list {
    position: absolute; left: 40px; top: 432px; list-style: none;
    font-size: 10.5px; line-height: 15px;
  }
  .workshop-list li::before {
    content: ""; display: inline-block; width: 5px; height: 5px;
    background: var(--dark); margin: 0 7px 1px 0;
  }
  .discount-box {
    position: absolute; left: 252px; top: 506px; width: 218px; height: 42px;
    background: var(--dark); color: var(--white);
    display: flex; align-items: center; padding: 0 10px;
    font-size: 10.5px; line-height: 13px;
  }
  .discount-value { font-size: 20px; font-weight: 700; margin-right: 10px; white-space: nowrap; }
  .back-contact {
    position: absolute; left: 0; top: 561px; width: 500px; height: 149px;
    background: var(--dark); color: var(--white);
  }
</style>
</head>
<body>

<svg width="0" height="0" style="position:absolute">
  <defs>
    <symbol id="icon-phone" viewBox="0 0 24 24">
      <path d="M6.6 10.8a15.1 15.1 0 0 0 6.6 6.6l2.2-2.2a1 1 0 0 1 1-.25 11.4 11.4 0 0 0 3.6.57 1 1 0 0 1 1 1V20a1 1 0 0 1-1 1A17 17 0 0 1 3 4a1 1 0 0 1 1-1h3.5a1 1 0 0 1 1 1c0 1.25.2 2.45.57 3.57a1 1 0 0 1-.25 1z" fill="currentColor"/>
    </symbol>
  </defs>
</svg>

<!-- Front page -->
<section class="flyer flyer--front">
  <div class="hero-photo" role="img" aria-label="Foto: die beiden Inhaber mit einem kleinen Hund auf einem hellen Sofa vor großen Fenstern"></div>
  <div class="brand-box"><span class="brand-name">Brandl's Werkhaus</span></div>

  <h1 class="headline" style="left:58px; top:378px;">Aus <b>alt</b><br>mach <b>neu!</b></h1>
  <p class="subline" style="left:61px; top:473px;">Lassen Sie ihre alte Küchen<br>in neuem Glanz erscheinen.</p>

  <div class="contact-area"></div>

  <ul class="services">
    <li class="service">
      <svg viewBox="0 0 24 24" fill="none" stroke="#fff" stroke-width="1.6"><rect x="3" y="10" width="8" height="11"/><rect x="13" y="10" width="8" height="11"/><rect x="5" y="3" width="4" height="5" fill="#fff"/><line x1="5" y1="14" x2="9" y2="14"/></svg>
      Küchenbau
    </li>
    <li class="service">
      <svg viewBox="0 0 24 24" fill="none" stroke="#fff" stroke-width="2"><path d="M12 3l3 5H9z" fill="#fff"/><path d="M4 17l3-5 3 5z" fill="#fff"/><path d="M20 17l-3-5-3 5z" fill="#fff"/><path d="M7 19h10"/></svg>
      Küchenrestauration
    </li>
    <li class="service">
      <svg viewBox="0 0 24 24" fill="none" stroke="#fff" stroke-width="1.6"><rect x="2" y="9" width="20" height="6" transform="rotate(-40 12 12)" fill="#fff"/></svg>
      Schränke nach Maß
    </li>
    <li class="service">
      <svg viewBox="0 0 24 24" fill="none" stroke="#fff" stroke-width="1.6"><rect x="3" y="4" width="18" height="3"/><rect x="5" y="7" width="14" height="14"/><path d="M9 21v-6a3 3 0 0 1 6 0v6"/></svg>
      Kaminverkleidungen
    </li>
  </ul>

  <h2 class="contact-title" style="left:41px; top:602px;">Kontaktieren Sie uns!</h2>
  <p class="contact-address" style="left:41px; top:629px;">Brandl's Werkhaus<br>Lindenhofer Weg 12&nbsp; I&nbsp; 68305 Mannheim</p>
  <div class="phone-button phone-button--dark" style="left:282px; top:614px;">
    <svg><use href="#icon-phone"/></svg>(0621) 591 82 07
  </div>
  <p class="website">www.brandls-werkhaus.de</p>
</section>

<!-- Back page -->
<section class="flyer flyer--back">
  <div class="project-grid">
    <div class="project-photo--grey" role="img" aria-label="Foto: graue Küche mit Dunstabzug"></div>
    <div class="project-photo--steel" role="img" aria-label="Foto: Küche vorher mit Kühlschrank und Backofen"></div>
    <div class="project-photo--wood" role="img" aria-label="Foto: alte Holzküche vorher"></div>
    <div class="project-photo--wood" role="img" aria-label="Foto: Hängeschrank aus Holz vorher"></div>
    <div class="project-photo--green" role="img" aria-label="Foto: Küche nachher mit Lichtleiste"></div>
    <div class="project-photo--steel" role="img" aria-label="Foto: Küche nachher mit Edelstahl-Kühlschrank"></div>
    <div class="project-photo--white" role="img" aria-label="Foto: renovierte Küche mit Holzarbeitsplatte"></div>
    <div class="project-photo--white" role="img" aria-label="Foto: renovierte Küche mit Spüle"></div>
  </div>

  <p class="back-brand">Brandl's Werkhaus</p>
  <p class="workshop-intro">Ihre Schreinerei aus Mannheim –<br>Traummöbel aus Holz:</p>
  <ul class="workshop-list">
    <li>Schlafzimmer</li>
    <li>Küchen / Esszimmer</li>
    <li>Büromöbel</li>
    <li>Wohnmöbel</li>
    <li>Treppen / Türen</li>
    <li>Kaminverkleidungen</li>
    <li>Sonderanfertigungen</li>
  </ul>

  <h1 class="headline" style="left:252px; top:378px;">Aus <b>alt</b><br>mach <b>neu!</b></h1>
  <p class="subline" style="left:254px; top:466px;">Lassen Sie ihre alte Küchen<br>in neuem Glanz erscheinen.</p>

  <div class="discount-box">
    <span class="discount-value">15 %</span>
    <span>Frühjahrsrabatt auf Ihre neue Küche – gültig bis 01.05.2025</span>
  </div>

  <div class="back-contact">
    <h2 class="contact-title" style="left:41px; top:41px;">Kontaktieren Sie uns!</h2>
    <p class="contact-address" style="left:41px; top:68px;">Brandl's Werkhaus<br>Lindenhofer Weg 12&nbsp; I&nbsp; 68305 Mannheim</p>
    <div class="phone-button phone-button--light" style="left:284px; top:53px;">
      <svg><use href="#icon-phone"/></svg>(0621) 591 82 07
    </div>
    <p class="website" style="top:113px;">www.brandls-werkhaus.de</p>
  </div>
</section>

</body>
</html>
```